Redo a PPT pres. - Real Estate in Brazil - Socially equitable investments in Social Housing

We need to redo the presentation attached. It is an institutional presentation to attract local and foreign investors to invest in Brazilian Social Housing Projects structured by our company "RTV".
A middle class of 100 million, a housing deficit of 9M, a strong political will & positive income generation trends constitute grounds for a significant demand in social housing.
This make a perfect scheme for investors to invest in Brazilian Social Housing.
"RTV", is a consulting "boutique" focused in Brazilian real estate, specialized in structuring, analyzing and originating Brazilian social housing projects.
RTV is part of the group RTP. RTP is structured to create value through each step of the residential real estate business - structuring, financing, sales, marketing and technology.
We would like to see designs that use mainly the color blue. The final design should communicate financial safety and professionalism. In order to reach our needs, the designer will need to have basic understanding of finance and investment in order to highlight the most important information.
The idea is to receive back the PPT with each page redesigned and an homogeneous identity.
To all designers,
Target Market(s)
Institutional Investors and wealthy individuals
Industry/Entity Type
Residential
Look and feel
Each slider illustrates characteristics of the customer's brand and the style your logo design should communicate.

```html
<!DOCTYPE html>
<html lang="en">
<head>
<meta charset="utf-8">
<title>RTV – Investor Presentation Slides</title>
<link href="https://fonts.googleapis.com/css2?family=Open+Sans:wght@400;600;700&family=Roboto+Condensed:wght@700&display=swap" rel="stylesheet">
<style>
  :root{
    --stage:#000;
    --paper:#ffffff;
    --navy-deep:#141c38;
    --slate:#4a5487;
    --city-top:#3d5a8f;
    --city-bottom:#1b2a52;
    --green:#7ac142;
    --green-bright:#8fd14f;
    --grey-cell:#dcdcdc;
    --grey-box:#ececec;
    --ink:#333;
    --muted:#8a8fa8;
  }
  *{box-sizing:border-box;margin:0;padding:0}
  html,body{width:1200px;height:520px;overflow:hidden;background:var(--stage);font-family:"Open Sans",Arial,sans-serif;color:var(--ink)}
  .slide{position:absolute;top:60px;width:530px;height:398px;background:var(--paper);overflow:hidden}
  .slide--demand{left:44px}
  .slide--track{left:623px}

  .side{position:absolute;left:0;top:0;width:196px;height:100%}
  .side__photo{position:absolute;inset:0;background:linear-gradient(180deg,var(--city-top) 0%,#2e4a7d 45%,var(--city-bottom) 100%)}
  .side__ribbon{position:absolute;left:59px;top:0;width:78px;height:66px;background:var(--navy-deep);clip-path:polygon(0 0,100% 0,100% 100%,50% 80%,0 100%);display:flex;justify-content:center;padding-top:20px}
  .brand{font-weight:400;font-size:15px;line-height:1;color:#fff;display:flex;align-items:center;gap:5px}
  .brand__mark{width:6px;height:6px;background:#fff}
  .badge{position:absolute;left:44px;top:162px;width:108px;height:108px;border-radius:50%;background:rgba(255,255,255,.35);display:flex;align-items:center;justify-content:center}
  .badge__inner{width:84px;height:84px;border-radius:50%;background:#fff;display:flex;align-items:center;justify-content:center;font-size:10px;color:var(--slate)}
  .side__headline{position:absolute;left:0;right:0;top:267px;text-align:center;font-family:"Roboto Condensed",Arial,sans-serif;font-weight:700;color:#fff;text-transform:uppercase;line-height:1.12}
  .side__headline .big{font-size:16px;display:block}
  .side__headline .small{font-size:11.5px;display:block;margin-top:6px}
  .side__band{position:absolute;left:0;right:0;bottom:0;height:60px;background:rgba(20,28,56,.85);display:flex;align-items:center;justify-content:center;text-align:center;padding:0 10px;color:var(--green-bright);font-size:7.5px;line-height:1.4}
  .slide--track .side__band{height:64px}

  .tab{position:absolute;height:17px;background:var(--slate);color:#fff;font-size:9px;line-height:17px;padding:0 20px 0 14px;white-space:nowrap;clip-path:polygon(0 0,100% 0,calc(100% - 8px) 50%,100% 100%,0 100%)}
  .tab--bold{font-weight:700;text-transform:uppercase}

  .chart{position:absolute;left:240px;top:64px}
  .legend{position:absolute;left:280px;top:219px;display:flex;gap:36px;font-size:6px}
  .legend__item{display:flex;align-items:center;gap:6px}
  .legend__swatch{width:11px;height:9px}

  .bullets{position:absolute;left:234px;top:288px;width:258px;list-style:none;font-size:6.2px;line-height:1.45}
  .bullets li{position:relative;padding-left:8px;margin-bottom:5px}
  .bullets li::before{content:"";position:absolute;left:0;top:3px;width:3px;height:3px;border-radius:50%;background:var(--ink)}
  .bullets b{font-weight:700}
  .bullets .note{color:var(--muted);display:block}

  .pager{position:absolute;right:14px;bottom:8px;display:flex;align-items:center;gap:4px;font-size:9px;font-weight:700;color:var(--slate)}
  .pager__arrow{color:#c8cbd8}

  .phase{position:absolute;left:239px;width:115px}
  .phase__title{height:24px;background:var(--green);color:#fff;font-size:8px;font-weight:700;line-height:24px;padding-left:14px}
  .phase__body{height:66px;background:var(--grey-box);font-size:5.6px;line-height:1.45;padding:8px 7px;list-style:none}
  .ledger{position:absolute;left:355px;width:114px;border-collapse:separate;border-spacing:0 2px;font-size:5.6px;table-layout:fixed}
  .ledger th{background:var(--slate);color:#fff;font-weight:600;text-align:left;padding:0 5px;height:19px;line-height:19px}
  .ledger td{background:var(--grey-cell);padding:0 5px;font-weight:600;height:13px;line-height:13px}
  .ledger col.label{width:74px}
  .trend{position:absolute;left:478px}
  .pending{height:38px;display:flex;align-items:center;justify-content:center;text-align:center;font-size:6px;line-height:1.3;padding:0}
  .summary{position:absolute;left:239px;top:334px;width:276px;font-size:6.4px;line-height:1.4}
</style>
</head>
<body>

<section class="slide slide--demand">
  <aside class="side">
    <div class="side__photo" role="img" aria-label="City skyline photograph in blue tones"></div>
    <div class="side__ribbon"><span class="brand"><span class="brand__mark"></span>RTV</span></div>
    <div class="badge"><div class="badge__inner">Green Light</div></div>
    <h1 class="side__headline"><span class="big">A middle class of<br>100 million people</span><span class="small">and still growing</span></h1>
    <p class="side__band">Positive demographics &amp; economic<br>environment will sustain the demand</p>
  </aside>

  <div class="tab" style="left:218px;top:30px;padding-left:26px">Number of people based on ages</div>

  <svg class="chart" width="230" height="140" viewBox="0 0 230 140" aria-label="Real wages growth and unemployment rate, 2005–2012">
    <g font-size="5.5" fill="#333" text-anchor="end">
      <text x="26" y="12">10%</text><text x="26" y="33">8%</text><text x="26" y="54">6%</text><text x="26" y="75">4%</text><text x="26" y="96">2%</text><text x="26" y="117">0%</text>
    </g>
    <line x1="30" y1="115" x2="218" y2="115" stroke="#999" stroke-width=".6"/>
    <g fill="#4a5487">
      <rect x="35" y="65" width="6" height="50"/>
      <rect x="59" y="51" width="6" height="64"/>
      <rect x="84" y="54" width="6" height="61"/>
      <rect x="108" y="56" width="6" height="59"/>
      <rect x="132" y="62" width="6" height="53"/>
      <rect x="157" y="45" width="6" height="70"/>
      <rect x="181" y="75" width="6" height="40"/>
      <rect x="205" y="58" width="6" height="57"/>
    </g>
    <polyline points="38,12 62,17 87,24 111,39 135,36 160,46 184,53 208,53" fill="none" stroke="#7ac142" stroke-width="3.5" stroke-linejoin="round"/>
    <g font-size="5.5" fill="#333" text-anchor="middle">
      <text x="38" y="132">2005</text><text x="62" y="132">2006</text><text x="87" y="132">2007</text><text x="111" y="132">2008</text><text x="135" y="132">2009</text><text x="160" y="132">2010</text><text x="184" y="132">2011</text><text x="208" y="132">2012</text>
    </g>
  </svg>
  <div class="legend">
    <span class="legend__item"><span class="legend__swatch" style="background:var(--slate)"></span>Real Wages Growth</span>
    <span class="legend__item"><span class="legend__swatch" style="background:var(--green)"></span>Unumployee Rate</span>
  </div>

  <div class="tab tab--bold" style="left:218px;top:266px;padding-left:14px">End Buyers</div>
  <ul class="bullets">
    <li>Aging population: Average number of persons per household shrunk from <b>3.7 in 1991 to 3.1 in 2010</b> (1). Expected to remain around 3.</li>
    <li>Projection of <b>12M more people by 2020.</b><span class="note">Natural increase in number of households / housing demand.</span></li>
    <li>Low and stable unemployment rate, <b>6%.</b></li>
    <li>Considerable growth in real wages, <b>average 5.5% from 2005-2012.</b><span class="note">20M more people will have entered Class C from 2008 to 2014.</span></li>
  </ul>
  <div class="pager"><span class="pager__arrow">&#10094;</span>06<span class="pager__arrow">&#10095;</span></div>
</section>

<section class="slide slide--track">
  <aside class="side">
    <div class="side__photo" role="img" aria-label="City skyline photograph in blue tones"></div>
    <div class="side__ribbon"><span class="brand"><span class="brand__mark"></span>RTV</span></div>
    <div class="badge"><div class="badge__inner">Green Light</div></div>
    <h1 class="side__headline"><span class="big">NHP: an impressive<br>track record</span></h1>
    <p class="side__band">Major component of the federal efforts on housing, NHP already shows outstanding results in less than 4 years, calling for its extension</p>
  </aside>

  <div class="tab tab--bold" style="left:214px;top:18px;padding-left:20px">Impressive Track Record</div>

  <div class="phase" style="top:42px">
    <div class="phase__title">NHP1 (2009-10)</div>
    <ul class="phase__body">
      <li>•Budget of R$34B</li>
      <li>•Reached target of 1M units in less than 2 yrs</li>
      <li>•Total sales value of R$51B</li>
    </ul>
  </div>
  <table class="ledger" style="top:52px">
    <colgroup><col class="label"><col></colgroup>
    <tr><th>MONTHLY WAGE (1)</th><th>AMOUNT</th></tr>
    <tr><td>Wages of 0- 3</td><td>574,123</td></tr>
    <tr><td>Wages of 0- 3</td><td>574,123</td></tr>
    <tr><td>Wages of 0- 3</td><td>574,123</td></tr>
    <tr><td>Wages of 0- 3</td><td>574,123</td></tr>
  </table>
  <svg class="trend" style="top:90px" width="40" height="24" viewBox="0 0 40 24" aria-hidden="true"><polygon points="0,0 40,0 20,24" fill="#7ac142"/></svg>

  <div class="phase" style="top:136px">
    <div class="phase__title">NHP1 (2011-14)</div>
    <ul class="phase__body">
      <li>•Budget of R$34B</li>
      <li>•Reached target of 1M units in less than 2 yrs</li>
      <li>•Total sales value of R$51B</li>
    </ul>
  </div>
  <table class="ledger" style="top:145px">
    <colgroup><col class="label"><col></colgroup>
    <tr><th>MONTHLY WAGE (1)</th><th>AMOUNT</th></tr>
    <tr><td>Wages of 0- 3</td><td>574,123</td></tr>
    <tr><td>Wages of 0- 3</td><td>574,123</td></tr>
    <tr><td>Wages of 0- 3</td><td>574,123</td></tr>
    <tr><td>Wages of 0- 3</td><td>574,123</td></tr>
    <tr><td>Wages of 0- 3</td><td>574,123</td></tr>
  </table>
  <svg class="trend" style="top:222px" width="40" height="24" viewBox="0 0 40 24" aria-hidden="true"><polygon points="0,0 40,0 20,24" fill="#7ac142"/></svg>

  <div class="phase" style="top:244px">
    <div class="phase__title">NHP1 (2015)</div>
    <div class="phase__body pending">? ? ? ?<br>? ? ? ? ? ?<br>? ? ? ?</div>
  </div>

  <p class="summary">After the success of NHP1 in 2009-10, the Brazilian government approved its continuation, and even doubled both the budget and targets. Surpassing initial projections, NHP2 (2011-14) will most likely reach its targets before the deadline. We then expect it to be further extended.</p>
  <div class="pager"><span class="pager__arrow">&#10094;</span>08<span class="pager__arrow">&#10095;</span></div>
</section>

</body>
</html>
```